Business card design and logo for plumbing bussiness

We are wanting a logo for a plumbing business is Queensland Australia. KRV Plumbing and Drainage will be doing works on domestic and commercial sites.
Plumbing, drainage and gas works. We are wanting something that will stand out and be noticed. Colours could be black blue and white but open for suggestions.

Target Market(s)

Builders and home renovators

Industry/Entity Type

Plumbing

Contact Information for Business Card

Miles Dorgan - Director
0417 582 913
miles@krvplumbing.example.com.au
QBCC: 847 2106
ABN: 52 319 407 281

Font styles to use
Sans Serif

Colors
000000

Requirements
Must have
• Clear defined branding

```html
<!DOCTYPE html>
<html lang="en">
<head>
<meta charset="utf-8">
<title>KRV Plumbing and Drainage – Business Card</title>
<link rel="stylesheet" href="https://fonts.googleapis.com/css2?family=Mulish:wght@400;500&display=swap">
<style>
  :root {
    --brand-blue: #0b37f2;
    --paper: #ffffff;
    --backdrop: #e6e7ea;
    --ink-blue: #1238e0;
    --icon-dark: #222222;
  }
  * { margin: 0; padding: 0; box-sizing: border-box; }
  html, body { width: 1200px; height: 1200px; overflow: hidden; }
  body {
    background: var(--backdrop);
    font-family: "Mulish", "Avenir", sans-serif;
    position: relative;
  }
  .card {
    position: absolute;
    left: 170px;
    width: 860px;
    height: 548px;
    overflow: hidden;
    box-shadow: 0 6px 24px rgba(0,0,0,0.12);
  }
  .card--front { top: 40px; background: var(--brand-blue); }
  .card--back  { top: 612px; background: var(--paper); }

  .front-brand {
    position: absolute;
    left: 470px;
    top: 448px;
    display: flex;
    align-items: center;
    gap: 14px;
    color: var(--paper);
    font-size: 23px;
    font-weight: 400;
    letter-spacing: 0.3px;
  }
  .brand-dot {
    width: 26px; height: 26px;
    border-radius: 50%;
    border: 3px solid currentColor;
    flex: none;
  }

  .back-brand {
    position: absolute;
    left: 150px;
    top: 220px;
    width: 180px;
    display: flex;
    flex-direction: column;
    align-items: center;
    gap: 14px;
    color: var(--ink-blue);
    font-size: 20px;
    font-weight: 500;
    text-align: center;
    line-height: 1.2;
  }
  .back-brand .brand-dot { width: 34px; height: 34px; border-width: 5px; }

  .contact-block {
    position: absolute;
    right: 140px;
    top: 148px;
    text-align: right;
    color: var(--ink-blue);
  }
  .person-name {
    font-size: 30px;
    font-weight: 500;
    letter-spacing: 0.5px;
    line-height: 1;
  }
  .person-role {
    font-size: 18px;
    font-weight: 400;
    margin-top: 4px;
    letter-spacing: 0.3px;
  }
  .contact-list { list-style: none; margin-top: 64px; }
  .contact-list li {
    font-size: 21px;
    line-height: 33.5px;
    position: relative;
    letter-spacing: 0.3px;
  }
  .contact-icon {
    position: absolute;
    right: -32px;
    top: 7px;
    width: 20px; height: 20px;
  }
</style>
</head>
<body>
  <section class="card card--front" aria-label="Card front">
    <div class="front-brand">
      <span class="brand-dot"></span>
      <span class="brand-name">KRV Plumbing and Drainage</span>
    </div>
  </section>

  <section class="card card--back" aria-label="Card back">
    <div class="back-brand">
      <span class="brand-dot"></span>
      <span class="brand-name">KRV Plumbing and Drainage</span>
    </div>

    <div class="contact-block">
      <h1 class="person-name">MILES DORGAN</h1>
      <p class="person-role">DIRECTOR</p>
      <ul class="contact-list">
        <li>0417 582 913
          <svg class="contact-icon" viewBox="0 0 20 20" aria-hidden="true">
            <circle cx="10" cy="10" r="8.5" fill="none" stroke="var(--icon-dark)" stroke-width="1.6"/>
            <path d="M7 5.5c-.8.4-1.3 1.2-1 2.3.6 2.6 2.9 5 5.5 5.9 1 .3 1.9-.1 2.4-.9l-1.6-1.4-1.1.7c-1.2-.6-2.2-1.6-2.8-2.8l.8-1.1z" fill="var(--icon-dark)"/>
          </svg>
        </li>
        <li>miles@krvplumbing.example.com.au
          <svg class="contact-icon" viewBox="0 0 20 20" aria-hidden="true">
            <g fill="none" stroke="var(--icon-dark)" stroke-width="1.5">
              <circle cx="10" cy="10" r="8.5"/>
              <ellipse cx="10" cy="10" rx="3.8" ry="8.5"/>
              <path d="M1.5 10h17M3 5.5h14M3 14.5h14M10 1.5v17"/>
            </g>
          </svg>
        </li>
        <li>QBCC: 847 2106</li>
        <li>ABN: 52 319 407 281
          <svg class="contact-icon" viewBox="0 0 20 20" aria-hidden="true">
            <circle cx="10" cy="10" r="8.5" fill="none" stroke="var(--icon-dark)" stroke-width="1.6"/>
            <path d="M7 5.5c-.8.4-1.3 1.2-1 2.3.6 2.6 2.9 5 5.5 5.9 1 .3 1.9-.1 2.4-.9l-1.6-1.4-1.1.7c-1.2-.6-2.2-1.6-2.8-2.8l.8-1.1z" fill="var(--icon-dark)"/>
          </svg>
        </li>
      </ul>
    </div>
  </section>
</body>
</html>
```